Brindlewood Business Card Design

Small Company
looking to ramp up work need business cards sick of everyone asking for a card
client base is broad.
keep it simple
Just want on the reverse of the card somewhere for me to write details for clients
appointments etc..
want to use the phrase
"Your safe, reliable and trust worthy Tradesmen"

Industry/Entity Type

Business

Contact Information for Business Card

Brindlewood Electrical Solutions Pty Ltd
Director Gregory Brindlewood
email - brindlewoodelectricalsolutions@zentromail.net
Ph - 03 95418276
Mobile - 0417592836
Domestic, Industrial, Commercial & Mining
Electrical, Solar, Communications & Fibre
REC: 41873

```html
<!DOCTYPE html>
<html lang="en">
<head>
<meta charset="utf-8">
<title>Brindlewood Electrical Solutions – Business Card</title>
<link rel="stylesheet" href="https://fonts.googleapis.com/css2?family=Roboto+Condensed:wght@400;700&display=swap">
<style>
  :root {
    --navy: #1f2a8c;
    --navy-deep: #141c66;
    --navy-light: #2c3aa8;
    --red: #e8323c;
    --paper: #ffffff;
    --paper-shade: #eceef2;
    --ink: #2a2a2e;
    --rule: #6b6e78;
    --write-line: rgba(255,255,255,.55);
    --backdrop: #e4e1dc;
  }
  * { box-sizing: border-box; margin: 0; padding: 0; }
  html, body {
    width: 1200px; height: 1024px; overflow: hidden;
    background: var(--backdrop);
    font-family: "Roboto Condensed", "Arial Narrow", sans-serif;
  }
  .canvas {
    width: 1200px; height: 1024px;
    display: flex; flex-direction: column; align-items: center; justify-content: center;
    gap: 34px;
  }
  .card {
    width: 800px; height: 457px; position: relative; overflow: hidden;
    box-shadow: 0 10px 28px rgba(0,0,0,.18);
  }

  /* Front */
  .card-front {
    background: linear-gradient(160deg, var(--paper) 40%, var(--paper-shade));
    border-bottom: 10px solid var(--navy);
  }
  .brand {
    position: absolute; left: 48px; top: 74px;
    display: flex; align-items: center; gap: 14px;
    color: var(--navy); font-weight: 400;
  }
  .brand-mark {
    width: 30px; height: 30px; border-radius: 50%; background: var(--navy); flex: none;
  }
  .brand-text { display: flex; flex-direction: column; line-height: 1; }
  .brand-name { font-size: 58px; letter-spacing: -0.5px; }
  .brand-sub { font-size: 22px; letter-spacing: 1.6px; text-transform: uppercase; margin-top: 4px; }

  .holder {
    position: absolute; right: 120px; top: 78px; text-align: right;
  }
  .holder-name { color: var(--navy); font-weight: 700; font-size: 26px; }
  .holder-role { color: var(--red); font-weight: 700; font-size: 26px; margin-top: 4px; }
  .licence {
    position: absolute; right: 26px; top: 40px;
    writing-mode: vertical-rl; transform: rotate(180deg);
    font-size: 18px; color: var(--ink);
  }
  .licence b { color: var(--red); font-weight: 700; }

  .divider {
    position: absolute; left: 0; right: 0; top: 218px; height: 1.5px; background: var(--rule);
  }
  .contacts {
    position: absolute; left: 48px; top: 262px; list-style: none;
    display: flex; flex-direction: column; gap: 18px;
  }
  .contact { display: flex; align-items: center; gap: 16px; font-size: 23px; color: var(--ink); }
  .contact-icon { width: 28px; height: 28px; flex: none; }

  /* Back */
  .card-back {
    background: radial-gradient(ellipse at 45% 35%, var(--navy-light), var(--navy) 55%, var(--navy-deep));
    color: var(--paper);
    display: flex; flex-direction: column; align-items: center;
    padding: 46px 64px 40px;
  }
  .back-brand {
    display: flex; align-items: center; gap: 18px; font-weight: 400;
  }
  .back-brand .brand-mark { background: var(--paper); width: 32px; height: 32px; }
  .back-brand .brand-name { font-size: 72px; }
  .back-brand .brand-sub { font-size: 26px; letter-spacing: 2.2px; }
  .tagline {
    margin-top: 22px; font-size: 22px; letter-spacing: .4px;
  }
  .services {
    margin-top: 12px; list-style: none;
    display: flex; justify-content: center; font-size: 17px; letter-spacing: .3px; white-space: nowrap;
  }
  .services li + li::before { content: "/"; margin: 0 12px; opacity: .85; }
  .write-in {
    margin-top: 28px; width: 100%; flex: 1;
    display: flex; flex-direction: column; justify-content: space-around;
  }
  .write-line { height: 0; border-bottom: 1.5px solid var(--write-line); }
</style>
</head>
<body>
<main class="canvas">

  <section class="card card-front" aria-label="Business card front">
    <div class="brand">
      <span class="brand-mark"></span>
      <span class="brand-text">
        <span class="brand-name">Brindlewood</span>
        <span class="brand-sub">Electrical Solutions</span>
      </span>
    </div>

    <div class="holder">
      <p class="holder-name">Gregory Brindlewood</p>
      <p class="holder-role">Director</p>
    </div>
    <p class="licence"><b>REC:</b> 41873</p>

    <div class="divider"></div>

    <ul class="contacts">
      <li class="contact">
        <svg class="contact-icon" viewBox="0 0 28 28" aria-hidden="true">
          <circle cx="14" cy="14" r="14" fill="var(--red)"/>
          <path d="M9.5 7.5l2.6-.4 1.3 3.2-1.6 1.2a8 8 0 0 0 3.7 3.7l1.2-1.6 3.2 1.3-.4 2.6c-5.6.6-10.6-4.4-10-10z" fill="#fff"/>
        </svg>
        <span>03 95418276</span>
      </li>
      <li class="contact">
        <svg class="contact-icon" viewBox="0 0 28 28" aria-hidden="true">
          <circle cx="14" cy="14" r="14" fill="var(--red)"/>
          <rect x="10" y="6.5" width="8" height="15" rx="1.4" fill="#fff"/>
          <rect x="11.3" y="8.5" width="5.4" height="9" fill="var(--red)"/>
          <circle cx="14" cy="19.5" r=".9" fill="var(--red)"/>
        </svg>
        <span>0417592836</span>
      </li>
      <li class="contact">
        <svg class="contact-icon" viewBox="0 0 28 28" aria-hidden="true">
          <circle cx="14" cy="14" r="14" fill="var(--red)"/>
          <rect x="7.5" y="9.5" width="13" height="9" rx="1" fill="#fff"/>
          <path d="M7.8 10l6.2 4.8 6.2-4.8" fill="none" stroke="var(--red)" stroke-width="1.3"/>
        </svg>
        <span>brindlewoodelectricalsolutions@zentromail.net</span>
      </li>
    </ul>
  </section>

  <section class="card card-back" aria-label="Business card back">
    <div class="back-brand">
      <span class="brand-mark"></span>
      <span class="brand-text">
        <span class="brand-name">Brindlewood</span>
        <span class="brand-sub">Electrical Solutions</span>
      </span>
    </div>
    <p class="tagline">Your safe, reliable and trustworthy Tradesmen</p>
    <ul class="services">
      <li>Domestic</li>
      <li>Industrial</li>
      <li>Commercial &amp; Mining Electrical</li>
      <li>Solar</li>
      <li>Communications &amp; Fibre</li>
    </ul>
    <div class="write-in" aria-label="Space to write client details and appointments">
      <div class="write-line"></div>
      <div class="write-line"></div>
      <div class="write-line"></div>
    </div>
  </section>

</main>
</body>
</html>
```